2020 Lone Ridge Crisis Alliance Conference Event flyer for annual conference held in Amarillo Texas

The Power of Connection

I need a flyer to send out via email. I The flyer will depict our theme, "The Power of Connection" event dates, website and costs. Association is Lone Ridge Crisis Alliance, date April 23-25, 2020, website www.loneridgealliance.org, Early Bird and Member discounts location Harborview Lodge, Amarillo Texas

page 2 will have sponsor info, and keynote description, can be 3 pages if absolutely necessary
: keynote speaker Martin Oakley, Martin is a retired Westbrook Roadway Patrol officer who spent more than 17 years patrolling the Silverfall Span Bridge. During that time he encountered hundreds of people who were troubled and had lost hope. They were ready to jump off the bridge and end their lives. Although a trained negotiator, Oakley also relied on his compassion, gentle voice, eye contact, and his innate ability to “listening to understand”. During his career, he encouraged more than 200 people not to jump, go over the bridge’s rail or come back to solid ground from where they had been standing precariously. These challenging, but rewarding efforts earned him the nickname, “Guardian of the Silverfall Span Bridge”. Retired, Oakley is now dedicating his life to promoting mental health awareness and suicide prevention across the globe.
Great sponsor opportunities available at www.Loneridgealliance.org sponsor letter attached for info on sponsor opportunities it is not necessary to include all info

i attached a mockup page 1 flyer that i really like but graphic designer did not complete this would give you an idea of what i am looking for on page 1 although it is missing a few elements

the Brookhaven (logo attached) is a champion sponsor, Plainsview Visitors Bureau (logo attached)

Target Market(s)

law enforcement, hospitals, mental health providers, court system,

Colors

Designer to choose colors to be used in the design.

Requirements
Must have
• theme -The Power of Connection
• website
• dates
• location
• costs
Nice to have
• prefer graphic related to theme
• Brookhaven is a large sponsor
• need to have 2-3 pages for all info
• include info on sponsor opportunities but does not have to include all info on attachment

```html
<!DOCTYPE html>
<html lang="en">
<head>
<meta charset="utf-8">
<title>The Power of Connection – 2020 Conference Flyer</title>
<link href="https://fonts.googleapis.com/css2?family=Barlow:wght@400;500;700&family=Barlow+Condensed:wght@400;500;700&family=Oswald:wght@600;700&family=Open+Sans:wght@400;600;700&display=swap" rel="stylesheet">
<style>
:root{
  --navy-deep:#0c1c2a;
  --navy:#16324a;
  --slate:#24445c;
  --red:#e0262f;
  --royal:#1d3c8f;
  --white:#ffffff;
  --ink:#222833;
  --card:#eeeff1;
  --stage-top:#ebe7e2;
  --stage-mid:#e6e6e6;
  --stage-low:#dcdcdc;
  --tick:#2f5fb5;
}
*{box-sizing:border-box;margin:0;padding:0}
html,body{width:1200px;height:2730px;overflow:hidden}
body{font-family:"Open Sans",Arial,sans-serif;color:var(--ink);position:relative;background:var(--stage-mid)}

.stage{position:absolute;left:0;width:1200px}
.stage-feature{top:0;height:1151px;background:var(--stage-top)}
.stage-spread{top:1151px;height:785px;background:var(--stage-mid)}
.stage-keynote{top:1936px;height:794px;background:var(--stage-low)}

.page{position:absolute;width:414px;height:585px;overflow:hidden;box-shadow:0 4px 14px rgba(0,0,0,.18)}
.page.enlarged{transform:scale(1.3);transform-origin:0 0;box-shadow:0 3px 10px rgba(0,0,0,.22)}

/* ---------- Cover ---------- */
.cover{background:linear-gradient(180deg,var(--navy) 0%,var(--navy-deep) 100%);color:var(--white);font-family:"Barlow",Arial,sans-serif}
.brand{position:absolute;display:flex;align-items:center;gap:8px}
.brand-dot{width:26px;height:26px;border-radius:50%;background:var(--white);flex:none}
.brand-name{font-family:"Barlow",Arial,sans-serif;font-weight:700;font-size:12px;line-height:1.15;letter-spacing:.06em;text-transform:uppercase;color:var(--white)}
.cover .brand{left:50%;top:52px;transform:translateX(-50%);width:190px}
.headline{position:absolute;left:41px;top:126px;line-height:1}
.headline .power{font-weight:700;font-size:42px;letter-spacing:.01em}
.headline .power small{font-weight:400;font-size:26px;margin-left:4px}
.headline .connection{display:block;color:var(--red);font-weight:700;font-size:42px;margin-top:3px;letter-spacing:.01em}
.conf-name{position:absolute;left:41px;top:223px;font-family:"Barlow Condensed",Arial,sans-serif;font-weight:500;font-size:17px;letter-spacing:.03em}
.dates{position:absolute;left:41px;top:244px;font-weight:500;font-size:44px;letter-spacing:.01em}
.year-tab{position:absolute;left:321px;top:184px;width:52px;height:104px;background:var(--red);display:flex;align-items:center;justify-content:center}
.year-tab span{transform:rotate(-90deg);font-weight:700;font-size:34px;letter-spacing:.04em}
.discounts{position:absolute;left:41px;top:304px;font-weight:500;font-size:16px;letter-spacing:.02em}
.location{position:absolute;left:41px;top:331px;font-weight:400;font-size:12.5px;letter-spacing:.02em}
.theme-visual{position:absolute;left:0;top:352px;width:414px;height:150px;background:radial-gradient(ellipse at 55% 40%,#f2c24a 0%,#c77a2a 18%,#4a3b3a 45%,rgba(12,28,42,0) 75%),linear-gradient(180deg,#16324a 0%,#3c3a46 55%,#0c1c2a 100%)}
.presented{position:absolute;left:0;right:0;top:507px;text-align:center;font-size:10px;font-weight:500}
.sponsor-row{position:absolute;left:0;right:0;top:525px;display:flex;justify-content:center;gap:18px;font-weight:700;font-size:10px}
.sponsor-row .tag{background:var(--white);color:var(--ink);padding:2px 6px}
.site{position:absolute;left:0;right:0;top:556px;text-align:center;font-size:10px;font-weight:500}

/* ---------- Sponsor page ---------- */
.sponsors{background:var(--card);font-family:"Open Sans",Arial,sans-serif}
.sp-head{position:absolute;left:0;top:0;width:414px;height:175px;background:var(--white)}
.sp-head svg{position:absolute;left:0;top:0}
.champ-tab{position:absolute;left:10px;top:20px;width:218px;height:26px;background:var(--red);color:var(--white);font-family:"Barlow",Arial,sans-serif;font-weight:700;font-size:17px;padding:2px 8px;letter-spacing:.02em}
.champ-list{position:absolute;left:18px;top:56px;list-style:none;color:var(--white);font-size:5.4px;font-weight:600;line-height:11px}
.champ-list li::before{content:"";display:inline-block;width:4px;height:4px;border-radius:50%;background:var(--red);margin-right:5px;vertical-align:middle}
.sp-head .brand{left:280px;top:52px;width:122px;flex-direction:column;gap:4px;text-align:center}
.sp-head .brand-dot{width:30px;height:30px;background:var(--royal)}
.sp-head .brand-name{color:var(--royal);font-size:9px}
.tiers{position:absolute;left:11px;top:182px;width:392px;display:grid;grid-template-columns:repeat(4,1fr);gap:3px}
.tier{background:#fafafa;min-height:214px;box-shadow:0 1px 2px rgba(0,0,0,.08)}
.tier.short{min-height:142px}
.tier-head{background:var(--red);color:var(--white);text-align:center;font-family:"Barlow",Arial,sans-serif;font-weight:700;font-size:8.5px;line-height:1.05;padding:4px 2px;min-height:28px;display:flex;flex-direction:column;justify-content:center}
.tier-role{font-size:5.4px;font-weight:700;text-align:center;padding:5px 4px 2px;line-height:1.2}
.tier ul{list-style:none;padding:3px 5px;font-size:5px;line-height:1.25}
.tier li{position:relative;padding-left:8px;margin-bottom:4px}
.tier li::before{content:"";position:absolute;left:0;top:1px;width:4px;height:4px;border:1px solid var(--tick);border-radius:50%}
.tier.note ul li{padding-left:0}
.tier.note ul li::before{display:none}
.tier.note ul{text-align:center}
.exhibitor{position:absolute;left:109px;top:496px;width:194px;height:20px;background:var(--red);color:var(--white);font-family:"Barlow",Arial,sans-serif;font-weight:700;font-size:8.5px;text-align:center;line-height:20px}
.exhibitor-items{position:absolute;left:109px;top:520px;width:194px;display:flex;justify-content:space-around;font-size:5px;list-style:none}
.exhibitor-items li::before{content:"";display:inline-block;width:4px;height:4px;border:1px solid var(--tick);border-radius:50%;margin-right:4px;vertical-align:middle}
.sp-foot{position:absolute;left:0;bottom:0;width:414px;height:27px;background:var(--royal);color:var(--white);font-size:8.5px;font-weight:600;text-align:center;line-height:27px}

/* ---------- Keynote page ---------- */
.keynote{background:linear-gradient(180deg,var(--slate) 0%,var(--navy-deep) 55%,#0a1622 100%);color:var(--white)}
.backdrop{position:absolute;left:170px;top:0;width:244px;height:300px;background:radial-gradient(ellipse at 50% 35%,rgba(70,90,110,.55) 0%,rgba(12,28,42,0) 70%)}
.speaker-photo{position:absolute;left:0;top:40px;width:236px;height:390px;background:radial-gradient(ellipse at 45% 30%,#b98f76 0%,#6b5850 28%,#2c3036 58%,rgba(12,28,42,0) 85%)}
.speaker-name{position:absolute;left:208px;top:108px;font-family:"Oswald",Arial,sans-serif;font-weight:700;font-size:56px;line-height:1.02;letter-spacing:.005em;color:#e9ecef}
.speaker-rule{position:absolute;left:212px;top:262px;width:150px;height:1px;background:rgba(255,255,255,.35)}
.bio{position:absolute;left:26px;top:424px;width:362px;font-size:6.4px;line-height:1.4}
.bio p{margin-bottom:6px}
.bio em{font-style:normal;color:var(--red);font-weight:600}
.k-foot{position:absolute;left:0;bottom:0;width:414px;height:26px;background:var(--red);color:var(--white);font-size:8.5px;font-weight:600;text-align:center;line-height:26px;letter-spacing:.04em}
</style>
</head>
<body>

<!-- Feature spread: cover and keynote -->
<section class="stage stage-feature">
  <article class="page cover enlarged" style="left:60px;top:195px">
    <div class="brand"><span class="brand-dot"></span><span class="brand-name">Lone Ridge Crisis Alliance</span></div>
    <h1 class="headline"><span class="power">THE POWER<small>OF</small></span><span class="connection">CONNECTION</span></h1>
    <p class="conf-name">LONE RIDGE CRISIS ALLIANCE CONFERENCE</p>
    <p class="dates">APRIL 23-25</p>
    <div class="year-tab"><span>2020</span></div>
    <p class="discounts">EARLY BIRD AND MEMBER DISCOUNTS</p>
    <p class="location">LOCATION: HARBORVIEW LODGE, AMARILLO TEXAS</p>
    <div class="theme-visual" role="img" aria-label="Two hands joined in a glowing handshake over a sunset horizon"></div>
    <p class="presented">Presented by:</p>
    <div class="sponsor-row"><span class="tag">The Brookhaven</span><span>Plainsview Visitors Bureau</span></div>
    <p class="site">www.loneridgealliance.org</p>
  </article>

  <article class="page keynote enlarged" style="left:602px;top:195px">
    <div class="backdrop" role="img" aria-label="Faint enlarged portrait of the keynote speaker"></div>
    <div class="speaker-photo" role="img" aria-label="Keynote speaker Martin Oakley speaking on stage"></div>
    <h2 class="speaker-name">MARTIN<br>OAKLEY</h2>
    <div class="speaker-rule"></div>
    <div class="bio">
      <p>During that time he encountered hundreds of people who were troubled and had lost hope. They were ready to jump off the bridge and end their lives. Although a trained negotiator, Oakley also relied on his compassion, gentle voice, eye contact, and his innate ability to “listening to understand”.</p>
      <p>During his career, he encouraged more than 200 people not to jump, go over the bridge’s rail or come back to solid ground from where they had been standing precariously. These challenging, but rewarding efforts earned him the nickname, <em>“Guardian of the Silverfall Span Bridge”.</em></p>
      <p>Retired, Oakley is now dedicating his life to promoting mental health awareness and suicide prevention across the globe.</p>
      <p>Martin is a retired Westbrook Roadway Patrol officer who spent more than 17 years patrolling the Silverfall Span Bridge.</p>
    </div>
    <div class="k-foot">www.loneridgealliance.org</div>
  </article>
</section>

<!-- Cover and sponsor page -->
<section class="stage stage-spread">
  <article class="page cover" style="left:127px;top:84px">
    <div class="brand"><span class="brand-dot"></span><span class="brand-name">Lone Ridge Crisis Alliance</span></div>
    <h1 class="headline"><span class="power">THE POWER<small>OF</small></span><span class="connection">CONNECTION</span></h1>
    <p class="conf-name">LONE RIDGE CRISIS ALLIANCE CONFERENCE</p>
    <p class="dates">APRIL 23-25</p>
    <div class="year-tab"><span>2020</span></div>
    <p class="discounts">EARLY BIRD AND MEMBER DISCOUNTS</p>
    <p class="location">LOCATION: HARBORVIEW LODGE, AMARILLO TEXAS</p>
    <div class="theme-visual" role="img" aria-label="Two hands joined in a glowing handshake over a sunset horizon"></div>
    <p class="presented">Presented by:</p>
    <div class="sponsor-row"><span class="tag">The Brookhaven</span><span>Plainsview Visitors Bureau</span></div>
    <p class="site">www.loneridgealliance.org</p>
  </article>

  <article class="page sponsors" style="left:628px;top:84px">
    <header class="sp-head">
      <svg width="414" height="175" viewBox="0 0 414 175" aria-hidden="true">
        <defs>
          <linearGradient id="headBand" x1="0" y1="0" x2="1" y2="1">
            <stop offset="0" stop-color="#16324a"/>
            <stop offset="1" stop-color="#1d3c8f"/>
          </linearGradient>
        </defs>
        <path d="M0 0H300C262 30 258 110 300 150C330 170 380 172 414 168V175H0Z" fill="url(#headBand)"/>
        <path d="M300 0C262 30 258 110 300 150C330 170 380 172 414 168" fill="none" stroke="#e0262f" stroke-width="5"/>
      </svg>
      <div class="champ-tab">CHAMPION $10,000</div>
      <ul class="champ-list">
        <li>Conference Sponsor</li>
        <li>Opportunity to introduce Speaker</li>
        <li>Full Page Program Ad</li>
        <li>Acknowledgments in Media Spotlight</li>
        <li>Personal Signage (color)</li>
        <li>Exhibit Booth</li>
        <li>10 Paid Registrations</li>
        <li>Sponsor Ribbons (10)</li>
        <li>Organizational Membership Lone Ridge Crisis Alliance</li>
      </ul>
      <div class="brand"><span class="brand-dot"></span><span class="brand-name">Lone Ridge Crisis Alliance</span></div>
    </header>

    <div class="tiers">
      <section class="tier">
        <div class="tier-head">Visionary<br>$8,000</div>
        <p class="tier-role">Award Luncheon Sponsor</p>
        <ul><li>Includes Opportunity to Introduce Speaker</li><li>Full Page Program Ad</li><li>Acknowledgments in Media Spotlights</li><li>Personalized Signage (Color)</li><li>Exhibit Booth</li><li>8 paid Registrations</li><li>Sponsor Ribbons (8)</li><li>Organizational Membership Lone Ridge</li></ul>
      </section>
      <section class="tier">
        <div class="tier-head">Leader<br>$5,000</div>
        <p class="tier-role">Morning Plenary Sponsor</p>
        <ul><li>Includes Opportunity to Introduce Speaker</li><li>Full Page Program Ad</li><li>Acknowledgments in Media Spotlights</li><li>Personalized Signage (Color)</li><li>Exhibit Booth</li><li>5 paid Registrations</li><li>Sponsor Ribbons (5)</li><li>Organizational Membership Lone Ridge</li></ul>
      </section>
      <section class="tier">
        <div class="tier-head">Builder<br>$2,500</div>
        <p class="tier-role">Workshop Sponsor</p>
        <ul><li>Includes Opportunity to Introduce Speaker</li><li>Half Page Program Ad</li><li>Acknowledgments in Media Spotlights</li><li>Group Signage (Color)</li><li>Exhibit Booth</li><li>3 paid Registrations</li><li>Sponsor Ribbons (3)</li><li>Organizational Membership Lone Ridge</li></ul>
      </section>
      <section class="tier">
        <div class="tier-head">Advocate<br>$1,000</div>
        <p class="tier-role">Workshop Sponsor</p>
        <ul><li>Includes Opportunity to Introduce Speaker</li><li>Half Page Program Ad</li><li>Acknowledgments in Media Spotlights</li><li>Group Signage (Color)</li><li>Exhibit Booth</li><li>2 paid Registrations</li><li>Sponsor Ribbons (2)</li><li>Organizational Membership Lone Ridge</li></ul>
      </section>
      <section class="tier short">
        <div class="tier-head">Friend<br>$500</div>
        <ul><li>Company Logo</li><li>Exhibit Booth</li><li>1 Paid Registration</li><li>Sponsor Ribbon (1)</li><li>Organizational Membership to Lone Ridge</li></ul>
      </section>
      <section class="tier short">
        <div class="tier-head">SPONSOR AN OFFICER<br>$500</div>
        <ul><li>Covers conference training for one officer</li><li>Company Logo and recognition in Print material</li></ul>
      </section>
      <section class="tier short note">
        <div class="tier-head">Coin Sponsor<br>$1000 (only1)<br>add-on to another package</div>
        <ul><li>Conference Coin will be designed for giveaway w/ sponsor logo on the back</li></ul>
      </section>
      <section class="tier short">
        <div class="tier-head">Program ADS</div>
        <ul><li>$250- 1/4 page ad</li><li>$500 1/2 page ad</li><li>$1000 Full page ad</li></ul>
      </section>
    </div>
    <div class="exhibitor">EXHIBITOR $250</div>
    <ul class="exhibitor-items"><li>Exhibit Booth</li><li>Print material</li></ul>
    <footer class="sp-foot">Register At: www.loneridgealliance.org</footer>
  </article>
</section>

<!-- Keynote page -->
<section class="stage stage-keynote">
  <article class="page keynote" style="left:393px;top:104px">
    <div class="backdrop" role="img" aria-label="Faint enlarged portrait of the keynote speaker"></div>
    <div class="speaker-photo" role="img" aria-label="Keynote speaker Martin Oakley speaking on stage"></div>
    <h2 class="speaker-name">MARTIN<br>OAKLEY</h2>
    <div class="speaker-rule"></div>
    <div class="bio">
      <p>During that time he encountered hundreds of people who were troubled and had lost hope. They were ready to jump off the bridge and end their lives. Although a trained negotiator, Oakley also relied on his compassion, gentle voice, eye contact, and his innate ability to “listening to understand”.</p>
      <p>During his career, he encouraged more than 200 people not to jump, go over the bridge’s rail or come back to solid ground from where they had been standing precariously. These challenging, but rewarding efforts earned him the nickname, <em>“Guardian of the Silverfall Span Bridge”.</em></p>
      <p>Retired, Oakley is now dedicating his life to promoting mental health awareness and suicide prevention across the globe.</p>
      <p>Martin is a retired Westbrook Roadway Patrol officer who spent more than 17 years patrolling the Silverfall Span Bridge.</p>
    </div>
    <div class="k-foot">www.loneridgealliance.org</div>
  </article>
</section>

</body>
</html>
```